RVK Entertainment

Logo for business card design

Target Market(s)

potential film investors and screenwriters

Industry/Entity Type

Business

Contact Information for Business Card

as shown, website here is a placeholder position

Requirements
Must have
• great visual appeal
Nice to have
• harmony of colors; must evoke spirit of
• U.S.-China cooperation

```html
<!DOCTYPE html>
<html lang="en">
<head>
<meta charset="UTF-8">
<title>RVK Entertainment – Business Card</title>
<link rel="stylesheet" href="https://fonts.googleapis.com/css2?family=Open+Sans:wght@600;700&display=swap">
<style>
  :root {
    --page-bg: #ffffff;
    --card-black: #070707;
    --card-glow: #2b2b2b;
    --gold-text: #f2c24a;
    --gold-light: #f7d77a;
    --gold-mid: #c8902a;
    --gold-deep: #7a5212;
    --pattern-black: #0b0906;
  }
  * { margin: 0; padding: 0; box-sizing: border-box; }
  html, body {
    width: 1200px; height: 819px; overflow: hidden;
    background: var(--page-bg);
  }
  .canvas { position: relative; width: 1200px; height: 819px; }
  .card {
    position: absolute; left: 30px; top: 84px;
    width: 1140px; height: 650px; overflow: hidden;
    background: radial-gradient(ellipse 520px 360px at 330px 300px, var(--card-glow) 0%, var(--card-black) 100%);
    font-family: "Open Sans", sans-serif;
    color: var(--gold-text);
  }
  .brand {
    position: absolute; left: 54px; top: 70px;
    display: flex; align-items: center; gap: 16px;
  }
  .brand-square { width: 34px; height: 34px; background: var(--gold-text); }
  .brand-name { font-size: 38px; font-weight: 700; line-height: 1; letter-spacing: 0.5px; }
  .tagline {
    position: absolute; left: 50px; top: 236px;
    font-size: 23px; font-weight: 600; line-height: 30px;
  }
  .contact-icon { position: absolute; width: 30px; height: 30px; }
  .contact-line {
    position: absolute; font-weight: 600; white-space: nowrap;
  }
  .contact-line.small { font-size: 20px; line-height: 28px; }
  .contact-line.large { font-size: 25px; line-height: 32px; }
  .pattern-panel {
    position: absolute; left: 613px; top: 0; width: 527px; height: 650px;
    background:
      radial-gradient(circle at 25% 20%, var(--gold-light) 0%, transparent 22%),
      radial-gradient(circle at 75% 45%, var(--gold-mid) 0%, transparent 28%),
      radial-gradient(circle at 35% 80%, var(--gold-light) 0%, transparent 24%),
      radial-gradient(circle at 85% 90%, var(--gold-mid) 0%, transparent 22%),
      linear-gradient(135deg, var(--gold-deep) 0%, var(--pattern-black) 50%, var(--gold-deep) 100%);
  }
</style>
</head>
<body>
<main class="canvas">
  <section class="card">
    <div class="brand">
      <span class="brand-square"></span>
      <span class="brand-name">RVK Entertainment</span>
    </div>

    <p class="tagline">Film business, professional Hollywood themed</p>

    <svg class="contact-icon" style="left:50px;top:330px" viewBox="0 0 24 24" aria-hidden="true">
      <path fill="var(--gold-text)" d="M6.6 10.8a15.1 15.1 0 0 0 6.6 6.6l2.2-2.2a1 1 0 0 1 1-.25 11.4 11.4 0 0 0 3.6.57 1 1 0 0 1 1 1V20a1 1 0 0 1-1 1A17 17 0 0 1 3 4a1 1 0 0 1 1-1h3.5a1 1 0 0 1 1 1c0 1.25.2 2.45.57 3.57a1 1 0 0 1-.25 1z"/>
    </svg>
    <p class="contact-line small" style="left:107px;top:316px">+18 2400 5512 0396</p>
    <p class="contact-line small" style="left:107px;top:347px">+18 3600 7129 4851</p>

    <svg class="contact-icon" style="left:56px;top:416px" viewBox="0 0 24 24" aria-hidden="true">
      <circle cx="12" cy="12" r="10" fill="var(--gold-text)"/>
      <path fill="none" stroke="var(--card-black)" stroke-width="1.6" d="M2 12h20M12 2c3 3 3 17 0 20M12 2c-3 3-3 17 0 20"/>
    </svg>
    <p class="contact-line small" style="left:114px;top:399px">HELLO@RVKFILMWORKS.COM</p>
    <p class="contact-line small" style="left:114px;top:433px">WWW.RVK-FILMWORKS.COM</p>

    <svg class="contact-icon" style="left:56px;top:506px" viewBox="0 0 24 24" aria-hidden="true">
      <path fill="var(--gold-text)" d="M12 2a7 7 0 0 0-7 7c0 5.2 7 13 7 13s7-7.8 7-13a7 7 0 0 0-7-7zm0 9.5A2.5 2.5 0 1 1 12 6.5a2.5 2.5 0 0 1 0 5z"/>
    </svg>
    <p class="contact-line small" style="left:114px;top:491px">YOUR CITY ADDRESS</p>
    <p class="contact-line large" style="left:114px;top:533px">218 Marlowe Ave #120, Seabrook</p>
    <p class="contact-line large" style="left:114px;top:586px">California 90417 USA</p>

    <div class="pattern-panel" role="img" aria-label="Gold baroque floral scroll pattern on black"></div>
  </section>
</main>
</body>
</html>
```